Nobody Left the Lantern Burning - Tom Halvery - CD Cover Design Project

Single Cover for CD & Online media e.g. Tunebox Graphics
The first song release from Tom Halvery will be the track 'Nobody Left the Lantern Burning'.
For the release the single requires artwork that is eye catching, seriously professional & meets the requirements of Disc Sprout, Tunebox and also a physical copy on CD.
Track listings for CD will be:
1. Nobody Left the Lantern Burning
2. Nobody Left the Lantern Burning - Instrumental
see details in this link:
http://members.discsprout-example.com/faq.aspx
http://selfmadesound.discsprout-example.com/2009/11/avoid-album-art-atrocities/
http://answers.quorvex-example.com/question/index?qid=20111015141433AAdDTmH
Any advice on this would be greatly appreciated,
I would also like the two logo's I have uploaded to be used,
one is the Tom Halvery logo and the other is for Milbrook & Tandy Records logo (please remove the R and replace with a C for copyright.)
There are four high res photo shopped pictures of Tom Halvery and another zip file of many others, it would be nice to include one of these maybe on the 2nd page or back of the CD. Please don't use them as the front cover.
I imagine an Art Deco illustration but please listen to the track and let it inspire you.
Good Luck
Updates
I don't feel this is what I'm looking for, the design needs to refelct a broken heart without being a picture of a broken heart
Reason: No design has been what we are after so far so the deadline has been extended and the budget increased.

```html
<!DOCTYPE html>
<html lang="en">
<head>
<meta charset="utf-8">
<title>Nobody Left the Lantern Burning – Tom Halvery – CD Cover</title>
<link rel="stylesheet" href="https://fonts.googleapis.com/css2?family=Oswald:wght@500;700&family=Parisienne&display=swap">
<style>
  :root {
    --bg: #000000;
    --rust-dark: #2e140a;
    --rust: #5e2c14;
    --rust-warm: #84431f;
    --flame: #e07a1c;
    --flame-bright: #f6a43e;
    --frame-dark: #2a1a12;
    --veil: rgba(222, 222, 222, 0.66);
    --scratch: rgba(235, 180, 130, 0.35);
    --ink-light: #ffffff;
    --ink-dark: #33231c;
    --label-maroon: #7a1f35;
  }
  html, body {
    margin: 0;
    padding: 0;
    width: 1200px;
    height: 800px;
    overflow: hidden;
    background: var(--bg);
  }
  .canvas {
    position: relative;
    width: 1200px;
    height: 800px;
    background: var(--bg);
  }
  .filter-defs { position: absolute; width: 0; height: 0; }
  .panel {
    position: absolute;
    top: 80px;
    width: 480px;
    height: 480px;
    overflow: hidden;
  }
  .panel--back { left: 81px; }
  .panel--front { left: 640px; }
  .spine {
    position: absolute;
    left: 591px;
    top: 80px;
    width: 20px;
    height: 480px;
    overflow: hidden;
    background: linear-gradient(180deg, var(--rust-dark), var(--rust) 40%, var(--rust-warm) 85%, var(--rust-dark));
  }
  .photo { position: absolute; inset: 0; }
  .photo--back {
    background:
      radial-gradient(ellipse 90px 120px at 300px 200px, rgba(190, 110, 80, 0.55), transparent 70%),
      radial-gradient(ellipse 70px 60px at 290px 120px, rgba(60, 40, 30, 0.6), transparent 70%),
      radial-gradient(ellipse 200px 120px at 300px 470px, rgba(215, 165, 150, 0.45), transparent 70%),
      radial-gradient(ellipse 260px 200px at 120px 300px, rgba(120, 60, 25, 0.5), transparent 75%),
      linear-gradient(170deg, #241008 0%, var(--rust) 40%, #6b4a22 80%, #3a2410 100%);
  }
  .photo--front {
    background:
      radial-gradient(ellipse 70px 230px at 455px 260px, rgba(250, 150, 45, 0.95), transparent 80%),
      radial-gradient(ellipse 60px 90px at 420px 120px, rgba(240, 140, 50, 0.7), transparent 80%),
      radial-gradient(ellipse 200px 90px at 110px 470px, rgba(230, 125, 30, 0.75), transparent 75%),
      radial-gradient(ellipse 140px 110px at 290px 120px, rgba(210, 150, 130, 0.35), transparent 75%),
      linear-gradient(170deg, #1e0c06 0%, #4a200e 25%, #6e3215 60%, #5a2610 100%);
  }
  .grunge { position: absolute; inset: 0; width: 100%; height: 100%; }
  .grunge--specks { mix-blend-mode: multiply; opacity: 0.75; }
  .grunge--mottle { mix-blend-mode: overlay; opacity: 0.7; }
  .edge-burn {
    position: absolute;
    inset: 0;
    background:
      linear-gradient(180deg, rgba(20, 8, 4, 0.75) 0%, rgba(20, 8, 4, 0) 22%),
      radial-gradient(ellipse 85% 85% at 50% 55%, transparent 60%, rgba(15, 6, 2, 0.55) 100%);
  }
  .artwork {
    position: absolute;
    left: 40px;
    top: 146px;
    width: 138px;
    height: 290px;
    box-sizing: border-box;
    border: 7px solid var(--frame-dark);
    border-bottom-width: 0;
    background: linear-gradient(180deg, var(--flame-bright), var(--flame) 55%, #a84e12);
  }
  .veil { position: absolute; background: var(--veil); }
  .veil__texture { position: absolute; inset: 0; width: 100%; height: 100%; mix-blend-mode: multiply; opacity: 0.55; }
  .veil--back { left: 336px; top: 92px; width: 144px; height: 344px; }
  .veil--front {
    left: 178px; top: 90px; width: 223px; height: 346px;
    background:
      radial-gradient(ellipse 50px 130px at 150px 120px, rgba(255, 255, 255, 0.35), transparent 75%),
      radial-gradient(ellipse 60px 140px at 40px 160px, rgba(120, 90, 80, 0.25), transparent 75%),
      var(--veil);
  }
  .veil--spine { left: 0; top: 87px; width: 20px; height: 345px; }
  .tracklist {
    position: absolute;
    left: 29px;
    top: 352px;
    margin: 0;
    padding: 0;
    list-style: none;
    font-family: "Oswald", sans-serif;
    font-weight: 500;
    font-size: 12.5px;
    line-height: 22px;
    letter-spacing: 0.2px;
    color: var(--ink-light);
  }
  .label-name {
    position: absolute;
    left: 344px;
    top: 398px;
    width: 130px;
    display: flex;
    align-items: center;
    gap: 5px;
    font-family: "Oswald", sans-serif;
    font-weight: 500;
    font-size: 10px;
    line-height: 12px;
    color: var(--label-maroon);
  }
  .label-name__mark { flex: none; width: 14px; height: 14px; background: var(--label-maroon); }
  .artist-name {
    position: absolute;
    left: 41px;
    top: 386px;
    margin: 0;
    font-family: "Oswald", sans-serif;
    font-weight: 700;
    color: var(--ink-dark);
    opacity: 0.88;
    line-height: 1;
  }
  .artist-name__first { display: block; font-size: 58px; letter-spacing: 3px; line-height: 56px; }
  .artist-name__last { display: block; font-size: 25px; letter-spacing: 3px; line-height: 28px; }
  .caption {
    position: absolute;
    top: 618px;
    width: 480px;
    margin: 0;
    text-align: center;
    font-family: "Parisienne", cursive;
    font-size: 50px;
    line-height: 80px;
    color: var(--ink-light);
  }
  .caption--back { left: 81px; }
  .caption--front { left: 640px; }
</style>
</head>
<body>
<div class="canvas">

  <svg class="filter-defs" aria-hidden="true">
    <defs>
      <filter id="specks" x="0" y="0" width="100%" height="100%">
        <feTurbulence type="fractalNoise" baseFrequency="0.9" numOctaves="3" seed="4"/>
        <feColorMatrix type="matrix" values="0 0 0 0 0.12  0 0 0 0 0.06  0 0 0 0 0.03  0 0 0 -2.4 1.45"/>
      </filter>
      <filter id="mottle" x="0" y="0" width="100%" height="100%">
        <feTurbulence type="fractalNoise" baseFrequency="0.018" numOctaves="4" seed="9"/>
        <feColorMatrix type="matrix" values="0 0 0 0 0.9  0 0 0 0 0.55  0 0 0 0 0.3  1.4 0 0 0 -0.4"/>
      </filter>
      <filter id="stains" x="0" y="0" width="100%" height="100%">
        <feTurbulence type="fractalNoise" baseFrequency="0.06" numOctaves="4" seed="2"/>
        <feColorMatrix type="matrix" values="0 0 0 0 0.45  0 0 0 0 0.42  0 0 0 0 0.4  0 0 0 -3 1.6"/>
      </filter>
    </defs>
  </svg>

  <section class="panel panel--back" aria-label="Back cover">
    <div class="photo photo--back" role="img" aria-label="Weathered photograph of Tom Halvery in glasses, in warm rust and brown tones"></div>
    <svg class="grunge grunge--mottle" aria-hidden="true"><rect width="480" height="480" filter="url(#mottle)"/></svg>
    <svg class="grunge grunge--specks" aria-hidden="true"><rect width="480" height="480" filter="url(#specks)"/></svg>
    <svg class="grunge" aria-hidden="true" stroke="var(--scratch)" stroke-width="0.7" fill="none">
      <line x1="10" y1="60" x2="180" y2="20"/><line x1="220" y1="90" x2="420" y2="10"/>
      <line x1="40" y1="160" x2="140" y2="110"/><line x1="0" y1="240" x2="260" y2="130"/>
      <line x1="60" y1="330" x2="210" y2="280"/><line x1="300" y1="40" x2="470" y2="70"/>
      <line x1="20" y1="420" x2="160" y2="390"/><line x1="120" y1="30" x2="150" y2="200"/>
      <line x1="250" y1="300" x2="330" y2="250"/><line x1="5" y1="120" x2="90" y2="140"/>
    </svg>
    <div class="edge-burn"></div>
    <div class="veil veil--back">
      <svg class="veil__texture" aria-hidden="true"><rect width="144" height="344" filter="url(#stains)"/></svg>
    </div>
    <ol class="tracklist">
      <li>1. Nobody Left the Lantern Burning</li>
      <li>2.Nobody Left the Lantern Burning - Instrumental</li>
    </ol>
    <div class="label-name">
      <span class="label-name__mark"></span>
      <span>MILBROOK &amp; TANDY RECORDS ©</span>
    </div>
  </section>

  <div class="spine" aria-label="Spine">
    <svg class="grunge grunge--specks" aria-hidden="true"><rect width="20" height="480" filter="url(#specks)"/></svg>
    <div class="veil veil--spine"></div>
  </div>

  <section class="panel panel--front" aria-label="Front cover">
    <div class="photo photo--front" role="img" aria-label="Warm orange flame light behind a scratched rust-toned surface"></div>
    <svg class="grunge grunge--mottle" aria-hidden="true"><rect width="480" height="480" filter="url(#mottle)"/></svg>
    <svg class="grunge grunge--specks" aria-hidden="true"><rect width="480" height="480" filter="url(#specks)"/></svg>
    <svg class="grunge" aria-hidden="true" stroke="var(--scratch)" stroke-width="0.7" fill="none">
      <line x1="30" y1="70" x2="200" y2="20"/><line x1="240" y1="60" x2="470" y2="5"/>
      <line x1="0" y1="130" x2="120" y2="100"/><line x1="330" y1="30" x2="460" y2="110"/>
      <line x1="110" y1="40" x2="300" y2="80"/><line x1="10" y1="210" x2="60" y2="150"/>
      <line x1="400" y1="420" x2="475" y2="360"/><line x1="190" y1="450" x2="320" y2="470"/>
      <line x1="60" y1="20" x2="140" y2="70"/><line x1="420" y1="200" x2="470" y2="260"/>
    </svg>
    <div class="edge-burn"></div>
    <div class="artwork" role="img" aria-label="Illustration of a silhouetted figure in a glowing orange doorway"></div>
    <div class="veil veil--front">
      <svg class="veil__texture" aria-hidden="true"><rect width="223" height="346" filter="url(#stains)"/></svg>
    </div>
    <h1 class="artist-name">
      <span class="artist-name__first">TOM</span>
      <span class="artist-name__last">HALVERY</span>
    </h1>
  </section>

  <p class="caption caption--back">back cover</p>
  <p class="caption caption--front">front cover</p>

</div>
</body>
</html>
```